Curriculum Card Design for Martial Arts System

We need an editable curriculum card design for a martial arts system. Would like to have our logo in background or highlighted on card. Each level will have their own separate card that can be printed onto a postcard sized paper (5x7 and 6x9). Each technique has three parts to it E, F, and S and would like them to be able to have a line or box which an instructor can initial or check next to each technique. Would like to have each curriculum card be straightforward with slight modern and futuristic touches similar to the emblem and logo.

Industry/Entity Type

Martial Art

Requirements
Must have
• Must be able to be edited as the curriculum techniques and moves may change or added/subracted.We are looking for something that is very easy to understand but also eye catching.
Should not have
• please Don't be boring in design.

```html
<!DOCTYPE html>
<html lang="en">
<head>
<meta charset="utf-8">
<title>Ascend Combat – Level One Curriculum Card</title>
<link rel="stylesheet" href="https://fonts.googleapis.com/css2?family=Lato:ital,wght@0,400;0,700;0,900;1,400;1,700&family=Libre+Baskerville:wght@700&display=swap">
<style>
  :root {
    --ink: #050505;
    --teal-deep: #0a3b3c;
    --teal-mid: #17605f;
    --brand-teal: #2fb7bb;
    --paper-light: #f7f7f7;
    --paper-shade: #d6d6d6;
    --rule: #1c4d4e;
    --text: #1a1a1a;
    --muted: #4a5c5c;
    --white: #ffffff;
  }
  * { box-sizing: border-box; margin: 0; padding: 0; }
  html, body { width: 900px; height: 1200px; overflow: hidden; background: #e9e9e9; }
  .card {
    position: relative;
    width: 900px;
    height: 1200px;
    overflow: hidden;
    background: radial-gradient(ellipse at 50% 55%, var(--paper-light) 0%, #ececec 45%, var(--paper-shade) 100%);
    font-family: "Lato", sans-serif;
    color: var(--text);
  }
  .card-header { position: absolute; inset: 0 0 auto 0; width: 900px; height: 470px; }
  .brand {
    position: absolute;
    left: 40px;
    top: 40px;
    width: 380px;
    display: flex;
    flex-direction: column;
    align-items: center;
    gap: 28px;
  }
  .brand-dot { width: 180px; height: 180px; border-radius: 50%; background: var(--teal-mid); }
  .brand-name {
    font-weight: 700;
    font-size: 40px;
    letter-spacing: 4px;
    color: var(--brand-teal);
    white-space: nowrap;
  }
  .level-badge {
    position: absolute;
    left: 530px;
    top: 346px;
    width: 284px;
    height: 50px;
    border-radius: 16px;
    background: linear-gradient(180deg, var(--teal-mid) 0%, var(--teal-deep) 70%);
    box-shadow: 0 10px 14px -8px rgba(10, 59, 60, 0.45);
    display: flex;
    align-items: center;
    justify-content: center;
    font-family: "Libre Baskerville", serif;
    font-weight: 700;
    font-size: 30px;
    color: var(--white);
    letter-spacing: 1px;
  }
  .curriculum {
    position: absolute;
    left: 60px;
    top: 474px;
    width: 780px;
    display: flex;
    flex-direction: column;
    gap: 12px;
  }
  .section {
    border: 2px solid var(--rule);
    border-radius: 14px;
    overflow: hidden;
    background: rgba(255, 255, 255, 0.45);
  }
  .section-title {
    height: 42px;
    display: flex;
    align-items: center;
    justify-content: center;
    background: linear-gradient(90deg, var(--teal-deep) 0%, var(--teal-mid) 50%, var(--teal-deep) 100%);
    color: var(--white);
    font-weight: 700;
    font-size: 22px;
    letter-spacing: 0.5px;
  }
  .grade-key, .technique-grid {
    display: grid;
    grid-template-columns: 1fr 1fr;
  }
  .grade-key {
    height: 20px;
    border-bottom: 1px solid var(--rule);
    background: rgba(23, 96, 95, 0.08);
  }
  .grade-key-col {
    display: flex;
    justify-content: flex-end;
    align-items: center;
    gap: 6px;
    padding-right: 14px;
  }
  .grade-key-col:first-child { border-right: 2px solid var(--rule); }
  .grade-key-col span {
    width: 20px;
    text-align: center;
    font-size: 13px;
    font-weight: 900;
    color: var(--muted);
  }
  .technique {
    height: 38px;
    display: flex;
    align-items: center;
    padding: 0 14px 0 20px;
    font-style: italic;
    font-size: 21px;
    border-bottom: 2px solid var(--rule);
    white-space: nowrap;
  }
  .technique:nth-child(odd) { border-right: 2px solid var(--rule); }
  .technique:nth-last-child(-n+2) { border-bottom: none; }
  .technique::before {
    content: "";
    width: 7px;
    height: 7px;
    border-radius: 50%;
    background: var(--text);
    margin-right: 8px;
    flex: none;
  }
  .technique-name { flex: 1; }
  .grade-boxes { display: flex; gap: 6px; flex: none; }
  .grade-box {
    width: 20px;
    height: 20px;
    border: 1.5px solid var(--rule);
    border-radius: 3px;
    background: var(--white);
  }
  .technique-grid.is-strong .technique { font-weight: 700; height: 44px; }
  .card-footer {
    position: absolute;
    left: 0;
    bottom: 0;
    width: 900px;
    height: 82px;
    background: linear-gradient(90deg, var(--teal-deep) 0%, var(--teal-mid) 50%, var(--teal-deep) 100%);
    display: flex;
    align-items: center;
    justify-content: center;
    color: var(--white);
    font-weight: 700;
    font-size: 25px;
    letter-spacing: 9px;
  }
</style>
</head>
<body>
  <main class="card">
    <svg class="card-header" viewBox="0 0 900 470" xmlns="http://www.w3.org/2000/svg">
      <defs>
        <clipPath id="header-shape">
          <path d="M0 0 H900 V282 C760 300 560 320 420 350 C280 380 140 430 0 445 Z"/>
        </clipPath>
        <linearGradient id="photo-tone" x1="0" y1="0" x2="1" y2="0">
          <stop offset="0" stop-color="#050505"/>
          <stop offset="0.25" stop-color="#3a3a3a"/>
          <stop offset="0.55" stop-color="#9a9a9a"/>
          <stop offset="0.8" stop-color="#6c6c6c"/>
          <stop offset="1" stop-color="#1a1a1a"/>
        </linearGradient>
      </defs>
      <path d="M0 0 H900 V282 C760 300 560 320 420 350 C280 380 140 430 0 445 Z" fill="#050505"/>
      <g clip-path="url(#header-shape)" role="img" aria-label="Black and white photograph of two martial artists in white uniforms sparring">
        <rect x="410" y="0" width="490" height="360" fill="url(#photo-tone)"/>
      </g>
      <path d="M0 456 C140 441 280 391 420 361 C560 331 760 311 900 293" fill="none" stroke="#b9b9b9" stroke-width="6" opacity="0.6"/>
    </svg>

    <div class="brand">
      <span class="brand-dot"></span>
      <span class="brand-name">ASCEND COMBAT</span>
    </div>

    <div class="level-badge">LEVEL ONE</div>

    <section class="curriculum">
      <div class="section">
        <h2 class="section-title">CONCEPT</h2>
        <div class="grade-key"><div class="grade-key-col"><span>E</span><span>F</span><span>S</span></div><div class="grade-key-col"><span>E</span><span>F</span><span>S</span></div></div>
        <div class="technique-grid">
          <p class="technique"><span class="technique-name">Closed Stance</span><span class="grade-boxes"><i class="grade-box"></i><i class="grade-box"></i><i class="grade-box"></i></span></p>
          <p class="technique"><span class="technique-name">Picture Frame Positioning</span><span class="grade-boxes"><i class="grade-box"></i><i class="grade-box"></i><i class="grade-box"></i></span></p>
          <p class="technique"><span class="technique-name">Hand Positioning</span><span class="grade-boxes"><i class="grade-box"></i><i class="grade-box"></i><i class="grade-box"></i></span></p>
          <p class="technique"><span class="technique-name">Point of Origin</span><span class="grade-boxes"><i class="grade-box"></i><i class="grade-box"></i><i class="grade-box"></i></span></p>
        </div>
      </div>
      <div class="section">
        <h2 class="section-title">OFFENSE</h2>
        <div class="grade-key"><div class="grade-key-col"><span>E</span><span>F</span><span>S</span></div><div class="grade-key-col"><span>E</span><span>F</span><span>S</span></div></div>
        <div class="technique-grid">
          <p class="technique"><span class="technique-name">Back Fist</span><span class="grade-boxes"><i class="grade-box"></i><i class="grade-box"></i><i class="grade-box"></i></span></p>
          <p class="technique"><span class="technique-name">Step Drag Body Punch</span><span class="grade-boxes"><i class="grade-box"></i><i class="grade-box"></i><i class="grade-box"></i></span></p>
          <p class="technique"><span class="technique-name">Body Punch</span><span class="grade-boxes"><i class="grade-box"></i><i class="grade-box"></i><i class="grade-box"></i></span></p>
          <p class="technique"><span class="technique-name">Round Kick</span><span class="grade-boxes"><i class="grade-box"></i><i class="grade-box"></i><i class="grade-box"></i></span></p>
          <p class="technique"><span class="technique-name">Step Drag Back Fist</span><span class="grade-boxes"><i class="grade-box"></i><i class="grade-box"></i><i class="grade-box"></i></span></p>
          <p class="technique"><span class="technique-name">Side Kick</span><span class="grade-boxes"><i class="grade-box"></i><i class="grade-box"></i><i class="grade-box"></i></span></p>
        </div>
      </div>
      <div class="section">
        <h2 class="section-title">MOVEMENT</h2>
        <div class="grade-key"><div class="grade-key-col"><span>E</span><span>F</span><span>S</span></div><div class="grade-key-col"><span>E</span><span>F</span><span>S</span></div></div>
        <div class="technique-grid is-strong">
          <p class="technique"><span class="technique-name">Neutral Bounce</span><span class="grade-boxes"><i class="grade-box"></i><i class="grade-box"></i><i class="grade-box"></i></span></p>
          <p class="technique"><span class="technique-name">Step Drag</span><span class="grade-boxes"><i class="grade-box"></i><i class="grade-box"></i><i class="grade-box"></i></span></p>
        </div>
      </div>
      <div class="section">
        <h2 class="section-title">DEFENSE/COUNTERS</h2>
        <div class="grade-key"><div class="grade-key-col"><span>E</span><span>F</span><span>S</span></div><div class="grade-key-col"><span>E</span><span>F</span><span>S</span></div></div>
        <div class="technique-grid is-strong">
          <p class="technique"><span class="technique-name">Wall Block</span><span class="grade-boxes"><i class="grade-box"></i><i class="grade-box"></i><i class="grade-box"></i></span></p>
          <p class="technique"><span class="technique-name">Push Checks</span><span class="grade-boxes"><i class="grade-box"></i><i class="grade-box"></i><i class="grade-box"></i></span></p>
        </div>
      </div>
    </section>

    <footer class="card-footer">www.ascendcombat.com</footer>
  </main>
</body>
</html>
```